Conference Room above Doorway Graphic Design

We would like to add a 36" Wide by 24" High Graphic Design to go over our Conference Room door.
We have a named our Conference Room the "Copper Loft" where great ideas are created and come to life! We would like the title "Copper Loft" included in the design and no other words. Our industry is the Inground Swimming Pool Industry. We would like to incorporate the swimming pool - water in the design.

```html
<!DOCTYPE html>
<html lang="en">
<head>
<meta charset="UTF-8">
<title>Copper Loft – Conference Room Door Graphic</title>
<link rel="stylesheet" href="https://fonts.googleapis.com/css2?family=Poppins:wght@700&display=swap">
<style>
  :root {
    --page-bg: #ffffff;
    --pool-deep: #1677b8;
    --pool-mid: #2fa9d6;
    --pool-light: #7fd8ec;
    --pool-teal: #3cbfdc;
    --lane-line: #0e4a6a;
    --bubble-center: #5ec6f0;
    --bubble-edge: #0a6dbb;
    --outline: #ffffff;
    --letter-light: #d6f6ff;
    --letter-mid: #5cccf0;
    --letter-deep: #1c8ccf;
  }
  html, body {
    margin: 0;
    padding: 0;
    width: 1200px;
    height: 1200px;
    overflow: hidden;
    background: var(--page-bg);
  }
  .canvas {
    position: relative;
    width: 1200px;
    height: 1200px;
  }
  .door-graphic {
    position: absolute;
    left: 100px;
    top: 267px;
    width: 1000px;
    height: 667px;
  }
  .lane-line {
    stroke: var(--lane-line);
    stroke-opacity: 0.55;
    stroke-width: 5;
    fill: none;
  }
  .room-name {
    font-family: "Poppins", sans-serif;
    font-weight: 700;
    fill: url(#letterWater);
    stroke: var(--outline);
    stroke-width: 2.5;
    text-anchor: middle;
  }
</style>
</head>
<body>
<div class="canvas">
  <svg class="door-graphic" viewBox="0 0 1000 667" xmlns="http://www.w3.org/2000/svg">
    <defs>
      <linearGradient id="poolWater" x1="0" y1="0" x2="1" y2="1">
        <stop offset="0" stop-color="var(--pool-deep)"/>
        <stop offset="0.3" stop-color="var(--pool-mid)"/>
        <stop offset="0.55" stop-color="var(--pool-teal)"/>
        <stop offset="0.8" stop-color="var(--pool-light)"/>
        <stop offset="1" stop-color="var(--pool-mid)"/>
      </linearGradient>
      <radialGradient id="bubbleFill" cx="0.5" cy="0.45" r="0.6">
        <stop offset="0" stop-color="var(--bubble-center)"/>
        <stop offset="1" stop-color="var(--bubble-edge)"/>
      </radialGradient>
      <linearGradient id="letterWater" x1="0" y1="0" x2="1" y2="1">
        <stop offset="0" stop-color="var(--letter-mid)"/>
        <stop offset="0.3" stop-color="var(--letter-light)"/>
        <stop offset="0.55" stop-color="var(--letter-mid)"/>
        <stop offset="0.8" stop-color="var(--letter-light)"/>
        <stop offset="1" stop-color="var(--letter-deep)"/>
      </linearGradient>
      <radialGradient id="ideaGlow" cx="0.5" cy="0.5" r="0.5">
        <stop offset="0" stop-color="#ffffff" stop-opacity="0.9"/>
        <stop offset="0.4" stop-color="#dff4ff" stop-opacity="0.45"/>
        <stop offset="1" stop-color="#ffffff" stop-opacity="0"/>
      </radialGradient>
    </defs>

    <rect class="pool-backdrop" x="0" y="0" width="1000" height="667" fill="url(#poolWater)"
          role="img" aria-label="Photograph of a tiled swimming pool seen through clear blue water"/>

    <g class="pool-lanes">
      <line class="lane-line" x1="0" y1="52" x2="1000" y2="22"/>
      <line class="lane-line" x1="0" y1="150" x2="1000" y2="108"/>
      <line class="lane-line" x1="0" y1="258" x2="1000" y2="208"/>
      <line class="lane-line" x1="0" y1="395" x2="1000" y2="318"/>
      <line class="lane-line" x1="0" y1="532" x2="1000" y2="422"/>
      <line class="lane-line" x1="0" y1="640" x2="1000" y2="560"/>
    </g>

    <path class="speech-bubble"
          d="M175 503 A411 280 0 1 1 270 565 L175 627 Z"
          fill="url(#bubbleFill)" stroke="var(--outline)" stroke-width="3" stroke-linejoin="round"/>

    <ellipse class="idea-glow" cx="505" cy="172" rx="240" ry="60" fill="url(#ideaGlow)"
             role="img" aria-label="Icon of a head in profile with a glowing light bulb inside, radiating light beams"/>

    <text class="room-name room-name-top" x="502" y="375" font-size="150">Copper</text>
    <text class="room-name room-name-bottom" x="502" y="543" font-size="132">Loft</text>
  </svg>
</div>
</body>
</html>
```